Feminine Health and Beauty Manufacture Needs simple clean box design

We need a box design to brand our multi line of products for women in the health and beauty market. The box will be 4" wide by 8" long and 3" deep.The design should incorporate colorful geometric or art deco patterns . I have attached a starting point for general direction on our first line called "Bloom" Luxury Bloom Mask . My sketch shows a chalk board black surrounded by the colorful pattern with the word Bloom in white script. looking for your creative input, design doesn't have to follow sketch, just and idea Good luck!
Reason: Out of town
Target Market(s)
25-60 year old women
Industry/Entity Type
Health
Look and feel

```html
<!DOCTYPE html>
<html lang="en">
<head>
<meta charset="utf-8">
<title>Bloom – Luxury Bloom Mask box panel</title>
<link rel="stylesheet" href="https://fonts.googleapis.com/css2?family=Great+Vibes&family=Kalam:wght@700&display=swap">
<style>
  :root {
    --page: #ffffff;
    --cream: #efe5cb;
    --teal: #6bb8a8;
    --ochre: #c9a245;
    --orange: #e8a25c;
    --chalkboard: #3b3b3b;
    --chalkboard-edge: #2f2f2f;
    --chalk: #f7f5ef;
  }
  * { margin: 0; padding: 0; box-sizing: border-box; }
  html, body {
    width: 1200px;
    height: 1000px;
    overflow: hidden;
    background: var(--page);
  }
  .canvas {
    position: relative;
    width: 1200px;
    height: 1000px;
    background: var(--page);
  }
  .pattern-band {
    position: absolute;
    left: 0;
    top: 202px;
    width: 1200px;
    height: 598px;
    background:
      radial-gradient(circle at 15% 30%, rgba(107,184,168,.55), transparent 28%),
      radial-gradient(circle at 85% 25%, rgba(201,162,69,.55), transparent 30%),
      radial-gradient(circle at 70% 90%, rgba(232,162,92,.45), transparent 30%),
      radial-gradient(circle at 20% 85%, rgba(107,184,168,.5), transparent 30%),
      var(--cream);
  }
  .chalkboard {
    position: absolute;
    left: 66px;
    top: 283px;
    width: 1064px;
    height: 435px;
    background: radial-gradient(ellipse at 45% 40%, #454545 0%, var(--chalkboard) 55%, var(--chalkboard-edge) 100%);
  }
  .chalk-art {
    position: absolute;
    inset: 0;
  }
  .brand-name {
    position: absolute;
    left: 112px;
    top: 300px;
    font-family: "Great Vibes", cursive;
    font-size: 250px;
    line-height: 1;
    color: var(--chalk);
  }
  .product-line {
    font-family: "Kalam", cursive;
    font-weight: 700;
    font-size: 50px;
    fill: var(--chalk);
  }
</style>
</head>
<body>
<main class="canvas">
  <div class="pattern-band" role="img" aria-label="Colourful paisley pattern in teal, ochre and orange on cream"></div>
  <section class="chalkboard" aria-label="Product label"></section>

  <svg class="chalk-art" width="1200" height="1000" viewBox="0 0 1200 1000" aria-hidden="true">
    <g class="frame-dots" stroke="var(--chalk)" stroke-width="4" stroke-linecap="round" stroke-dasharray="0 10" fill="none">
      <line x1="160" y1="298" x2="405" y2="298"/>
      <line x1="795" y1="298" x2="1040" y2="298"/>
      <line x1="160" y1="702" x2="405" y2="702"/>
      <line x1="795" y1="702" x2="1040" y2="702"/>
      <line x1="82" y1="360" x2="82" y2="640"/>
      <line x1="1114" y1="360" x2="1114" y2="640"/>
    </g>
    <g class="banner" transform="rotate(-13 800 560)" stroke="var(--chalk)" fill="none" stroke-linecap="round">
      <path d="M540 500 L1060 500" stroke-width="5"/>
      <line x1="510" y1="518" x2="1090" y2="518" stroke-width="4" stroke-dasharray="0 10"/>
      <line x1="510" y1="602" x2="1090" y2="602" stroke-width="4" stroke-dasharray="0 10"/>
      <path d="M560 622 Q530 622 530 640 Q530 656 550 652 L1060 622" stroke-width="5"/>
      <text class="product-line" x="800" y="585" text-anchor="middle" stroke="none">Luxury Bloom Mask</text>
    </g>
  </svg>

  <h1 class="brand-name">Bloom</h1>
</main>
</body>
</html>
```